BASIC website restyle: graphic + coding

I need a restyle of our present website. Same contents, but better graphic.
It will be temporary until we'll have defined the strategy and so we'll have the definitive one.
I would need a fast job including coding.

I uploaded some picture that you're free to use.
I also extended of 1 day, no more extensions will be possible.

```html
<!DOCTYPE html>
<html lang="en">
<head>
<meta charset="utf-8">
<title>Verdale</title>
<link rel="stylesheet" href="https://fonts.googleapis.com/css2?family=Open+Sans:wght@400;600;700&display=swap">
<style>
  :root {
    --green: #0b8a3e;
    --green-dark: #0a6b33;
    --slate: #344352;
    --slate-frame: #6b7b8b;
    --ink: #333d47;
    --text-light: #ffffff;
    --rule: #d9dcdf;
    --forest-deep: #2c2a18;
    --forest-mid: #4f6a2c;
    --forest-light: #a9b48a;
  }
  * { box-sizing: border-box; margin: 0; padding: 0; }
  html, body { width: 1200px; height: 777px; overflow: hidden; background: #fff; }
  body { font-family: "Open Sans", Arial, sans-serif; color: var(--ink); position: relative; }

  .stripe {
    position: absolute; left: 0; width: 1200px; height: 3px;
    background: repeating-linear-gradient(90deg, var(--green) 0 40px, var(--slate) 40px 80px);
  }
  .stripe--top { top: 0; }
  .stripe--bottom { top: 774px; }

  .site-header { position: absolute; top: 3px; left: 0; width: 1200px; height: 86px; }
  .brand { position: absolute; left: 207px; top: 18px; }
  .brand__name { font-size: 42px; font-weight: 700; color: var(--green); letter-spacing: -1px; line-height: 48px; }

  .main-nav { position: absolute; right: 208px; top: 35px; display: flex; gap: 31px; }
  .main-nav a { font-size: 13px; color: var(--ink); text-decoration: none; text-transform: uppercase; }
  .main-nav a.is-active { color: var(--green); }

  .hero { position: absolute; top: 89px; left: 0; width: 1200px; height: 387px; }
  .hero__photo {
    position: absolute; inset: 0;
    background:
      radial-gradient(ellipse at 58% 30%, var(--forest-light) 0%, rgba(169,180,138,0) 45%),
      linear-gradient(90deg, var(--forest-deep) 0%, var(--forest-mid) 35%, #6f7d4a 55%, var(--forest-mid) 75%, var(--forest-deep) 100%);
  }
  .hero__photo::after {
    content: ""; position: absolute; left: 0; right: 0; bottom: 0; height: 110px;
    background: linear-gradient(180deg, rgba(70,120,30,0) 0%, #4d8a24 100%);
  }
  .hero__band { position: absolute; left: 0; top: 387px; width: 1200px; height: 5px; background: var(--green); }
  .hero__title {
    position: absolute; left: 246px; top: 160px; width: 336px; height: 58px;
    background: rgba(11,138,62,0.92); color: var(--text-light);
    font-size: 26px; font-weight: 700; line-height: 58px; text-align: center; letter-spacing: 0.3px;
  }
  .hero__arrow { position: absolute; top: 160px; width: 56px; height: 56px; }
  .hero__arrow--prev { left: 152px; }
  .hero__arrow--next { left: 993px; }

  .features { position: absolute; top: 514px; left: 208px; width: 784px; display: flex; gap: 35px; }
  .feature {
    width: 374px; height: 139px; background: var(--slate);
    border: 1px solid #26313c; position: relative;
  }
  .feature__media {
    position: absolute; left: 15px; top: 14px; width: 107px; height: 109px;
    border: 5px solid var(--slate-frame);
  }
  .feature__media--fire { background: linear-gradient(160deg, #6b3b3a 0%, #8a3c22 50%, #e07a1e 85%, #f2b233 100%); }
  .feature__media--field { background: linear-gradient(180deg, #8fb070 0%, #6e9e45 45%, #a8c489 100%); }
  .feature__body { position: absolute; left: 140px; top: 14px; width: 225px; }
  .feature__title { font-size: 20px; font-weight: 400; color: var(--text-light); line-height: 26px; }
  .feature__text { font-size: 11px; color: var(--text-light); line-height: 15px; margin-top: 2px; }
  .feature__more {
    display: inline-block; margin-top: 8px; margin-left: 2px; width: 72px; height: 25px;
    background: var(--green); color: var(--text-light); font-size: 12px; line-height: 25px;
    text-align: center; text-decoration: none;
  }

  .site-footer { position: absolute; top: 686px; left: 208px; width: 784px; border-top: 1px solid var(--rule); }
  .copyright { position: absolute; top: 26px; left: 0; font-size: 11.5px; color: var(--ink); white-space: nowrap; }
  .copyright a { color: var(--green); text-decoration: none; }
  .social { position: absolute; top: 21px; right: 0; display: flex; gap: 5px; }
  .social__item { width: 24px; height: 24px; border-radius: 50%; background: var(--slate); display: block; }
  .social__item--first { background: var(--green); }
</style>
</head>
<body>
  <div class="stripe stripe--top"></div>

  <header class="site-header">
    <div class="brand">
      <div class="brand__name">VERDALE</div>
    </div>
    <nav class="main-nav">
      <a href="#" class="is-active">Home</a>
      <a href="#">Emberless2</a>
      <a href="#">Fieldsense</a>
      <a href="#">Technology</a>
      <a href="#">Contact us</a>
    </nav>
  </header>

  <section class="hero">
    <div class="hero__photo" role="img" aria-label="Misty redwood forest with a fallen log among green ferns"></div>
    <div class="hero__band"></div>
    <svg class="hero__arrow hero__arrow--prev" viewBox="0 0 56 56" aria-label="Previous slide">
      <circle cx="28" cy="28" r="28" fill="#0a6b33" fill-opacity="0.9"/>
      <polyline points="33,15 21,28 33,41" fill="none" stroke="#fff" stroke-width="2"/>
    </svg>
    <h1 class="hero__title">INTERNET OF THINGS</h1>
    <svg class="hero__arrow hero__arrow--next" viewBox="0 0 56 56" aria-label="Next slide">
      <circle cx="28" cy="28" r="28" fill="#0a6b33" fill-opacity="0.9"/>
      <polyline points="23,15 35,28 23,41" fill="none" stroke="#fff" stroke-width="2"/>
    </svg>
  </section>

  <main class="features">
    <article class="feature">
      <div class="feature__media feature__media--fire" role="img" aria-label="Wildfire burning in a forest"></div>
      <div class="feature__body">
        <h2 class="feature__title">Forest fires</h2>
        <p class="feature__text">Lorem Ipsum is simply dummy text of the printing and typesetting industry. Lorem Ipsum has been the industry's standard</p>
        <a href="#" class="feature__more">More</a>
      </div>
    </article>
    <article class="feature">
      <div class="feature__media feature__media--field" role="img" aria-label="Watering can watering young crops in a field"></div>
      <div class="feature__body">
        <h2 class="feature__title">Agriculture</h2>
        <p class="feature__text">Lorem Ipsum is simply dummy text of the printing and typesetting industry. Lorem Ipsum has been the industry's standard</p>
        <a href="#" class="feature__more">More</a>
      </div>
    </article>
  </main>

  <footer class="site-footer">
    <p class="copyright">Copyright © 2013 All right reserved by <a href="#">verdale.com</a></p>
    <div class="social">
      <a href="#" class="social__item social__item--first" aria-label="Social link"></a>
      <a href="#" class="social__item" aria-label="Social link"></a>
      <a href="#" class="social__item" aria-label="Social link"></a>
    </div>
  </footer>

  <div class="stripe stripe--bottom"></div>
</body>
</html>
```